Wine Label for a Sweet Wine Called "Glimmora"

We need a wine label that will be used for both a sweet red and a sweet white wine. The very important thing to remember is the target market for these wines is: young American women who love sweet wines and they also spend a lot of their money on their hair, clothes, jewelry, nails. They LOVE Glimmora (Glimmora is a word used to describe flashy accessories, jewelry, decoration.) This label needs to be eye catching, showy, fun, glittery. Please put the brand name, "Glimmora," big, and then in smaller but still readable words underneath the label or somewhere on the label: Sweet, Sophisticated, Red (or white). (An example of what I mean is attached). To differentiate between the two color wines you can suggest color changes to differentiate between the red label and the white label but the label design itself should be the same. Ultimately, the label can be the exact same label for both white and red as long as it looks good on a white wine (a greenish/yellow wine in a clear glass bottle) and a red wine (a dark color wine in a dark bottle).

I've attached an example of the text size relationship between the word Glimmora and the words to go underneath or elsewhere on the label, but you can certainly play with this-- it is just a suggestion of the text size relationship, and definitely NOT at all mandatory that you use any of these fonts.

You can pick the size of the label but try to stay within normal wine label sizes, meaning don't go bigger than approx. 3.5 inches wide and 5 inches tall.

Target Market(s)

Young American women who love sweet wines and spend a lot of money on their hair, clothes, jewelry, nails. They love Glimmora (Glimmora is a word that means flashy accessories, jewelry, decoration)

Requirements
Must have
• It needs to be flashy, glittery, fun, eye catching, memorable
Nice to have
• It shouldn't be too too ultra feminine! The target market is strong independent women and we also have men who will buy it too.

```html
<!DOCTYPE html>
<html lang="en">
<head>
<meta charset="UTF-8">
<title>Glimmora — Sweet Red Wine Label</title>
<link rel="stylesheet" href="https://fonts.googleapis.com/css2?family=Cinzel:wght@500;600&family=Cormorant+SC:wght@500;600&display=swap">
<style>
  :root {
    --backdrop: #050505;
    --label-black: #141414;
    --label-shade: #0b0b0b;
    --label-sheen: #262626;
    --gold: #c9a94f;
    --gold-light: #e6cd7e;
    --flourish-grey: rgba(190, 190, 190, 0.16);
  }

  html, body {
    margin: 0;
    padding: 0;
    width: 1200px;
    height: 1000px;
    overflow: hidden;
    background: var(--backdrop);
  }

  .canvas {
    position: relative;
    width: 1200px;
    height: 1000px;
    background: var(--backdrop);
  }

  .wine-label {
    position: absolute;
    left: 300px;
    top: 140px;
    width: 600px;
    height: 720px;
    background:
      radial-gradient(ellipse at 40% 30%, var(--label-sheen) 0%, var(--label-black) 45%, var(--label-shade) 100%);
  }

  .label-frame {
    position: absolute;
    inset: 0;
    width: 600px;
    height: 720px;
  }

  .flourish-area {
    position: absolute;
    left: 150px;
    top: 150px;
    width: 340px;
    height: 320px;
    border-radius: 50%;
    background: radial-gradient(ellipse at center, var(--flourish-grey) 0%, rgba(190,190,190,0.06) 50%, transparent 72%);
  }

  .brand-block {
    position: absolute;
    left: 0;
    right: 0;
    top: 215px;
    text-align: center;
  }

  .brand-name {
    margin: 0;
    font-family: "Cinzel", "Times New Roman", serif;
    font-weight: 600;
    font-size: 76px;
    letter-spacing: 4px;
    line-height: 1;
    color: var(--gold);
  }

  .wine-descriptor {
    margin: 18px 0 0;
    font-family: "Cormorant SC", "Georgia", serif;
    font-weight: 600;
    font-size: 22px;
    letter-spacing: 3px;
    color: var(--gold-light);
  }

  .vintage {
    position: absolute;
    left: 0;
    right: 0;
    bottom: 110px;
    margin: 0;
    text-align: center;
    font-family: "Cormorant SC", "Georgia", serif;
    font-weight: 600;
    font-size: 26px;
    letter-spacing: 5px;
    color: var(--gold);
  }
</style>
</head>
<body>
<main class="canvas">
  <section class="wine-label">
    <svg class="label-frame" viewBox="0 0 600 720" aria-hidden="true">
      <path d="M36 14 H564 A22 22 0 0 0 586 36 V684 A22 22 0 0 0 564 706 H36 A22 22 0 0 0 14 684 V36 A22 22 0 0 0 36 14 Z"
            fill="none" stroke="var(--gold)" stroke-width="2.5"/>
      <path d="M44 26 H556 A18 18 0 0 0 574 44 V676 A18 18 0 0 0 556 694 H44 A18 18 0 0 0 26 676 V44 A18 18 0 0 0 44 26 Z"
            fill="none" stroke="var(--gold)" stroke-width="1.2"/>
    </svg>

    <div class="flourish-area" role="img" aria-label="Faint silver calligraphic script monogram flourish behind the brand name"></div>

    <div class="brand-block">
      <h1 class="brand-name">GLIMMORA</h1>
      <p class="wine-descriptor">SWEET | SOPHISTICATED | RED</p>
    </div>

    <p class="vintage">MMXVI</p>
  </section>
</main>
</body>
</html>
```